PFM Web Design Project

I'm looking for a small, friendly,functional, information based website. If you go through the attachments, you would know the nature of the business.
Updates

Hi,

I have uploaded a picture of the CEO, Mr. Rafael Okonto DPAMV member. Please feel free to use it whereever appropriate.

Thanks!

Reason: Still not satisfied with the designs. Waiting to get layouts from top designers invited to the project.

Hello, I have uploaded some references. I like the colours used on the bar and would w

Example of a we page . I like this layout for the inside pages.

I am changing the tabs on my website to:

Home
About us
Services
Contact us

The services tab will have three sub pages:

Immigration
Education
AccommodationAccommodation

Target Market(s)

Young international students willing to come to Canada to study, young international students willing to immigrate to Canada, parents of the students

Industry/Entity Type

Business

Requirements
Must have
• PFM HOME
ABOUT US
CONTACT
SERVICES
TAG LINE

The website should look n feel trendy, smart, current, factual, trustworthy etc....
Nice to have
• I am looking for a bold, attractive, eye catchy home page with less text! Something that makes a statement....
Should not have
• No Clip art, flash animation, no bells n whistles please

```html
<!DOCTYPE html>
<html lang="en">
<head>
<meta charset="utf-8">
<title>PFM – Taking You Onwards</title>
<link href="https://fonts.googleapis.com/css2?family=Open+Sans:wght@400;600;700&family=Russo+One&display=swap" rel="stylesheet">
<style>
  :root {
    --bg-dark: #6a0008;
    --bg-light: #a3050f;
    --white: #ffffff;
    --ink: #1d1d1d;
    --grey-text: #7a7a7a;
    --slate: #4a5560;
    --red: #e0101c;
    --orange: #f28a1a;
    --orange-dark: #d9700a;
    --hero-grey: #dedede;
    --mission: #6b000b;
  }
  * { margin: 0; padding: 0; box-sizing: border-box; }
  html, body { width: 1200px; height: 1093px; overflow: hidden; }
  body {
    position: relative;
    background: linear-gradient(180deg, var(--bg-dark) 0%, var(--bg-light) 60%, var(--bg-light) 100%);
    font-family: "Open Sans", sans-serif;
    color: var(--ink);
  }
  .page {
    position: absolute; left: 96px; top: 50px; width: 1008px; height: 992px;
    background: var(--white); border-radius: 4px; overflow: hidden;
  }
  .brand { position: absolute; left: 32px; top: 40px; }
  .brand-row { display: flex; align-items: center; gap: 10px; }
  .brand-mark { width: 34px; height: 34px; background: var(--red); }
  .brand-name { font-family: "Open Sans", sans-serif; font-weight: 700; font-size: 56px; line-height: 1; color: var(--ink); }
  .brand-sub { margin-top: 10px; font-size: 15px; color: #555; font-weight: 600; }
  .tagline {
    position: absolute; right: 35px; top: 66px;
    font-family: "Russo One", sans-serif; font-size: 36px; color: var(--ink); letter-spacing: 1px;
  }
  .tagline span { color: var(--red); }
  .nav { position: absolute; right: 35px; top: 122px; display: flex; gap: 26px; list-style: none; }
  .nav li { font-size: 16.5px; color: var(--grey-text); }
  .nav li.active { color: var(--orange); }
  .hero {
    position: absolute; left: 0; top: 201px; width: 1008px; height: 372px;
    background: linear-gradient(110deg, #e9e9e9 0%, var(--hero-grey) 40%, #d8d8d8 100%);
  }
  .hero-title { position: absolute; left: 51px; top: 140px; font-size: 32px; color: var(--slate); letter-spacing: 0.5px; font-weight: 400; }
  .hero-title span { color: var(--red); }
  .hero-lead { position: absolute; left: 51px; top: 179px; font-size: 14px; color: var(--slate); }
  .btn {
    position: absolute; left: 51px; top: 216px; width: 177px; height: 38px;
    background: linear-gradient(180deg, var(--orange) 0%, var(--orange-dark) 100%);
    border: 1px solid #c26208; box-shadow: 0 2px 3px rgba(0,0,0,0.3);
    color: var(--white); font-size: 14.5px; font-weight: 600; text-align: center; line-height: 36px; padding-left: 46px;
  }
  .hero-photo {
    position: absolute; left: 487px; top: 173px; width: 461px; height: 400px;
    background: linear-gradient(90deg, #e6d9d4 0%, #cfc2bd 45%, #3b3b40 65%, #2a2a2e 100%);
    border-radius: 180px 180px 0 0;
  }
  .mission {
    position: absolute; left: 20px; top: 591px; width: 966px; height: 93px;
    background: var(--mission); color: var(--white);
    font-size: 12px; line-height: 19.5px; padding: 15px 23px;
  }
  .mission b { font-weight: 700; }
  .section-title { position: absolute; font-size: 18.5px; font-weight: 400; color: var(--ink); }
  .section-title span { color: var(--red); }
  .services-title { left: 22px; top: 706px; }
  .contact-title { left: 789px; top: 706px; }
  .service { position: absolute; top: 750px; width: 239px; }
  .service-card { height: 159px; background: var(--white); box-shadow: 0 0 4px rgba(0,0,0,0.25); padding: 5px; }
  .service-img { width: 100%; height: 100%; }
  .service-label { margin-top: 13px; text-align: center; font-family: Arial, sans-serif; font-size: 14px; letter-spacing: 0.5px; color: var(--ink); line-height: 16px; }
  .service-label.active { color: var(--orange); }
  .contact { position: absolute; left: 795px; top: 745px; font-size: 12.5px; color: #555; line-height: 16px; }
  .contact dt { font-weight: 700; color: var(--ink); font-size: 12px; margin-top: 14px; }
  .contact dt:first-child { margin-top: 0; }
  .copyright { position: absolute; left: 0; top: 1059px; width: 1200px; text-align: center; color: var(--white); font-family: Arial, sans-serif; font-size: 11.5px; }
</style>
</head>
<body>
  <div class="page">
    <header>
      <div class="brand">
        <div class="brand-row"><div class="brand-mark"></div><div class="brand-name">PFM</div></div>
        <div class="brand-sub">Pathway Futures Management</div>
      </div>
      <div class="tagline">Taking You <span>Onwards</span></div>
      <ul class="nav">
        <li class="active">Home</li>
        <li>About Us</li>
        <li>Services</li>
        <li>Contact</li>
        <li>PFM Mission</li>
      </ul>
    </header>

    <section class="hero">
      <h1 class="hero-title">DARE TO DREAM <span>CANADIAN</span></h1>
      <p class="hero-lead">Your best partner for immigration &amp; education solution in Canada.</p>
      <div class="btn">LEARN MORE</div>
    </section>
    <div class="hero-photo" role="img" aria-label="Photo of a smiling young student with a backpack and a young man in a business suit"></div>

    <p class="mission">At <b>PFM</b> we are committed to our customer centered philosophy. Our mission is to help our clients achieve their goals by providing them with world class customer service that is both reliable and competitively superior. We are driven by our core values: ethics, expertise and leadership. We believe that honesty paves the way for true success. We have been there. We know what it takes.</p>

    <h2 class="section-title services-title">OUR <span>SERVICES</span></h2>
    <div class="service" style="left:25px">
      <div class="service-card"><div class="service-img" role="img" aria-label="Photo of a hand holding a Canadian passport" style="background:linear-gradient(135deg,#e8dcd2 0%,#1f2a44 55%,#141c30 100%)"></div></div>
      <div class="service-label">IMMIGRATION</div>
    </div>
    <div class="service" style="left:275px">
      <div class="service-card"><div class="service-img" role="img" aria-label="Photo of the word education chalked on a green board" style="background:linear-gradient(160deg,#5aa592 0%,#3f8a78 60%,#2f6e60 100%)"></div></div>
      <div class="service-label active">EDUCATION</div>
    </div>
    <div class="service" style="left:527px">
      <div class="service-card"><div class="service-img" role="img" aria-label="Photo of a stack of books with a red graduation cap and diploma" style="background:radial-gradient(ellipse at 55% 55%,#c9332c 0%,#8a4a3a 35%,#f4f1ee 75%)"></div></div>
      <div class="service-label">STUDENT ACCOMMODATION<br>SERVICES</div>
    </div>

    <h2 class="section-title contact-title">CONTACT <span>US</span></h2>
    <dl class="contact">
      <dt>ADDRESS :</dt>
      <dd>418 Linden Avenue, Barrie,<br>Ontario, L4N 2K7 Canada</dd>
      <dt>PHONE :</dt>
      <dd>(705) 555 0142<br>(705) 555 0187</dd>
      <dt>EMAIL :</dt>
      <dd>info@pathwayfutures.com</dd>
    </dl>
  </div>
  <footer class="copyright">Copyright © 2013 PathwayFuturesManagement. All Rights Reserved.</footer>
</body>
</html>
```